Business Card Design Project 4 Construction Business

I am after a creative, but sleek and simple/ clean business card design. This design will form the basis of future items and might include a logo or simply a creative way to lay out the text of my company name 'keldmoor builds'
I like the simplicity of black and white however I would also be happy to see a splash of colour introduced somehow to give the text some interest and make it stand out.
I would like a double sided card.
I am young (ish!) and professional, offering construction and project management services, what I don't want is the traditional builders type card featuring a cheesy hammer/ saw image etc.
As the company name, keldmoor builds, suggests, we focus on working closely and collaboratively together, in synergy with all stakeholders involved in the projects that we undertake
Industry/Entity Type
Construction

```html
<!DOCTYPE html>
<html lang="en">
<head>
<meta charset="utf-8">
<title>Keldmoor Builds – Business Card</title>
<link rel="stylesheet" href="https://fonts.googleapis.com/css2?family=Questrial&family=Arimo:wght@400&display=swap">
<style>
  :root {
    --page-bg: #ffffff;
    --card-bg: #332a1a;
    --band-bg: #3e3320;
    --brand-orange: #f59e4c;
    --name-gold: #d9a65c;
  }
  * { margin: 0; padding: 0; box-sizing: border-box; }
  html, body {
    width: 1200px;
    height: 833px;
    overflow: hidden;
    background: var(--page-bg);
  }
  .canvas {
    position: relative;
    width: 1200px;
    height: 833px;
  }
  .business-card {
    position: absolute;
    left: 377px;
    top: 285px;
    width: 446px;
    height: 264px;
    background: var(--card-bg);
    border-top-left-radius: 60px;
    overflow: hidden;
  }
  .brand-band {
    position: absolute;
    left: 0;
    top: 86px;
    width: 100%;
    height: 80px;
    background: var(--band-bg);
    display: flex;
    align-items: center;
    justify-content: center;
  }
  .brand-name {
    font-family: "Questrial", sans-serif;
    font-weight: 400;
    font-size: 40px;
    letter-spacing: -0.5px;
    color: var(--brand-orange);
    line-height: 1;
  }
  .contact-person {
    position: absolute;
    right: 28px;
    top: 202px;
    text-align: right;
    font-family: "Arimo", sans-serif;
    color: var(--name-gold);
  }
  .person-name {
    font-size: 17px;
    letter-spacing: 0.6px;
    line-height: 22px;
  }
  .person-role {
    font-size: 15px;
    letter-spacing: 0.8px;
    line-height: 20px;
  }
</style>
</head>
<body>
  <main class="canvas">
    <section class="business-card">
      <div class="brand-band">
        <p class="brand-name">keldmoor builds</p>
      </div>
      <div class="contact-person">
        <p class="person-name">Tobin Carver</p>
        <p class="person-role">Director</p>
      </div>
    </section>
  </main>
</body>
</html>
```